Real Estate "For Sale" Sign for construction company

We need a sign that we can use to hang on a post and place on the road when we sell a property. The sign will be simple and will need to mainly feature our logo (files attached), as well as the words "For Sale", and then our phone number "(555) 617 3489". The sign will hang on a post that'll look something like the attached picture.

Target Market(s)

Home buyers

Industry/Entity Type

Real Estate

Font styles to use
Serif
Sans Serif

Colors
0054AA
0677BA
7BADD7
CADEEF
E8F1F8
0094D4
00A9DD
6FCCEA
C7EBF8
E9F6FB

Requirements
Must have
• For Sale & our phone number

```html
<!DOCTYPE html>
<html lang="en">
<head>
<meta charset="UTF-8">
<title>Highland Pine Realty – For Sale Sign</title>
<link href="https://fonts.googleapis.com/css2?family=Lexend:wght@400&family=Roboto+Condensed:wght@700&display=swap" rel="stylesheet">
<style>
  :root {
    --page-bg: #ffffff;
    --sign-bg: #8fd6f5;
    --band-bg: #2c3356;
    --band-text: #ffffff;
    --phone-text: #2f3b80;
    --brand-text: #3a86cf;
    --brand-mark: #2d5fa8;
    --shadow: rgba(0, 0, 0, 0.28);
  }
  * { margin: 0; padding: 0; box-sizing: border-box; }
  html, body {
    width: 1200px;
    height: 598px;
    overflow: hidden;
    background: var(--page-bg);
  }
  .canvas {
    position: relative;
    width: 1200px;
    height: 598px;
  }
  .sign {
    position: absolute;
    left: 422px;
    top: 44px;
    width: 356px;
    height: 470px;
    background: var(--sign-bg);
  }
  .sign-shadow {
    position: absolute;
    left: 412px;
    top: 524px;
    width: 376px;
    height: 22px;
    border-radius: 50%;
    background: radial-gradient(ellipse at center, var(--shadow) 0%, rgba(0,0,0,0.12) 55%, rgba(0,0,0,0) 75%);
  }
  .brand {
    position: absolute;
    top: 52px;
    left: 0;
    width: 100%;
    display: flex;
    flex-direction: column;
    align-items: center;
  }
  .brand-mark {
    width: 104px;
    height: 104px;
    border-radius: 50%;
    background: var(--brand-mark);
  }
  .brand-name {
    margin-top: 46px;
    font-family: "Lexend", sans-serif;
    font-weight: 400;
    font-size: 25px;
    color: var(--brand-text);
    letter-spacing: 0.2px;
    white-space: nowrap;
  }
  .sale-band {
    position: absolute;
    top: 301px;
    left: 0;
    width: 100%;
    height: 75px;
    background: var(--band-bg);
    display: flex;
    align-items: center;
    justify-content: center;
    gap: 18px;
  }
  .sale-label {
    font-family: "Roboto Condensed", sans-serif;
    font-weight: 700;
    font-size: 50px;
    color: var(--band-text);
    letter-spacing: 0.5px;
    line-height: 1;
  }
  .sale-icon { width: 46px; height: 46px; }
  .phone {
    position: absolute;
    top: 400px;
    left: 0;
    width: 100%;
    text-align: center;
    font-family: "Roboto Condensed", sans-serif;
    font-weight: 700;
    font-size: 40px;
    color: var(--phone-text);
    line-height: 1;
  }
</style>
</head>
<body>
  <main class="canvas">
    <section class="sign">
      <div class="brand">
        <div class="brand-mark" aria-hidden="true"></div>
        <div class="brand-name">Highland Pine Realty</div>
      </div>
      <div class="sale-band">
        <span class="sale-label">FOR SALE</span>
        <svg class="sale-icon" viewBox="0 0 46 46" aria-hidden="true">
          <circle cx="23" cy="23" r="21" fill="none" stroke="#ffffff" stroke-width="2.2"/>
          <path d="M13 22 L23 13 L33 22 M16 20 V32 H30 V20" fill="none" stroke="#ffffff" stroke-width="2.2" stroke-linejoin="round" stroke-linecap="round"/>
          <rect x="20" y="25" width="6" height="7" fill="none" stroke="#ffffff" stroke-width="2"/>
        </svg>
      </div>
      <div class="phone">(555) 617 3489</div>
    </section>
    <div class="sign-shadow" aria-hidden="true"></div>
  </main>
</body>
</html>
```